Web Design Project - veltrimo

I'm building an agency for marketing solutions but also medical education and patients education for pharmaceutical companies, medical societies and patient advocacy groups. We want to be perceived as the most innovative in the market. We work through design thinking solutions for campaigns and services.
I love some websites based on Swiss style design like www.plorvex.net
We are a small group of designers, physicians and creatives working together to deliver the best experiences in our market.
We decided to also use design crowd expecting that we maybe found a great idea we didn't thought about yet.
Updates

I'm extending it for more 2 weeks

Reason: I need the best design you can. Only PSD. No code needed. Love Swiss style, like qualdor 5 and plorvex.net I'm extending the deadline until get something great. Willing to extend as much as needed.

Target Market(s)

Pharmaceutical companies, physicians, medical societies, patients advocacy groups

Industry/Entity Type

Pharmaceutical

Font styles to use
Other font styles liked:
• Helvetia family

Colors

Designer to choose colors to be used in the design.

Requirements
Must have
• Must be innovative like www.plorvex.net
Nice to have
• Cool menus
Should not have
• Not to appear too much Comercial. We like to be a boutique in this market. Craftsmen working with less clients at time but delivering precious stones.

```html
<!DOCTYPE html>
<html lang="en">
<head>
<meta charset="utf-8">
<title>veltrimo</title>
<link rel="stylesheet" href="https://fonts.googleapis.com/css2?family=Lato:wght@400;700&family=Roboto:wght@300;400&family=Lora:ital@1&display=swap">
<style>
:root{
  --page:#1c1c1c;
  --bar:#141414;
  --tile:#262626;
  --tile-active:#2a2a2a;
  --brand-red:#c8292d;
  --project-blue:#2e4f6e;
  --text-strong:#f2f2f2;
  --text-head:#dcdcdc;
  --text-body:#8c8c8c;
  --text-muted:#6a6a6a;
  --icon:#bdbdbd;
}
*{margin:0;padding:0;box-sizing:border-box}
html,body{width:1200px;height:1000px;overflow:hidden}
body{background:var(--page);font-family:"Roboto",Arial,sans-serif;position:relative}
.topbar{position:absolute;left:0;top:0;width:1200px;height:46px;background:var(--bar)}
.menu-toggle{position:absolute;left:181px;top:15px}
.site-name{position:absolute;left:228px;top:14px;font-family:"Lato",sans-serif;font-weight:700;font-size:14px;color:#555}
.nav-item{position:absolute;top:0;width:45px;height:46px;display:flex;align-items:center;justify-content:center}
.nav-item.is-active{background:var(--tile-active)}
.footer-band{position:absolute;left:0;top:862px;width:1200px;height:138px;background:var(--bar)}
.tile{position:absolute;width:135px;height:135px}
.media{position:absolute}
.card{position:absolute;background:var(--tile);padding:12px 10px}
.card h3{font-family:"Lato",sans-serif;font-weight:700;font-size:10.5px;line-height:14px;color:var(--text-head);margin-bottom:9px}
.card p{font-weight:300;font-size:8px;line-height:14.5px;color:var(--text-body)}
.brand-tile{left:316px;top:83px;background:var(--brand-red);display:flex;align-items:center;justify-content:center}
.brand-tile span{font-family:"Lato",sans-serif;font-weight:700;font-size:19px;color:#fff;letter-spacing:-.2px}
.intro{position:absolute;left:460px;top:83px;width:279px;height:280px;background:var(--tile);padding:28px 16px}
.intro p{font-weight:300;font-size:21px;line-height:28px;color:#9a9a9a;letter-spacing:-.4px}
.intro b{font-weight:400;color:var(--text-strong)}
.intro .cta{display:block;margin-top:16px;font-size:8.5px;color:#cfcfcf;font-weight:400}
.project{position:absolute;left:604px;top:519px;width:279px;height:281px;background:var(--project-blue)}
.project h2{position:absolute;left:5px;top:4px;font-family:"Lora",serif;font-style:italic;font-weight:400;font-size:15px;line-height:20px;color:#fff}
.project h2 em{color:#8fb1cc;font-style:italic}
.project small{position:absolute;left:5px;top:45px;font-family:"Lora",serif;font-style:italic;font-size:7px;color:#5d7f9c}
.contact{position:absolute;left:604px;top:809px;width:279px;height:135px;background:var(--tile);padding:18px 28px}
.contact h2{font-family:"Lato",sans-serif;font-weight:700;font-size:18px;color:#fff;margin-bottom:18px}
.contact li{list-style:none;display:flex;align-items:center;font-size:8.5px;color:#aaa;height:21px}
.contact li svg{width:18px;margin-right:1px}
.copyright{position:absolute;left:316px;top:964px;font-size:8px;color:#888}
.social{position:absolute;top:964px;width:7px;height:7px;border-radius:50%;background:#9a9a9a}
</style>
</head>
<body>
<header class="topbar">
  <svg class="menu-toggle" width="17" height="13" viewBox="0 0 17 13"><rect y="0" width="17" height="2" fill="#ddd"/><rect y="5.5" width="17" height="2" fill="#ddd"/><rect y="11" width="17" height="2" fill="#ddd"/></svg>
  <div class="site-name">veltrimo</div>
  <a class="nav-item is-active" style="left:694px"><svg width="12" height="11" viewBox="0 0 12 11"><path d="M6 0 0 5.5h1.5V11h3.5V7.5h2V11h3.5V5.5H12z" fill="var(--icon)"/></svg></a>
  <a class="nav-item" style="left:748px"><svg width="15" height="11" viewBox="0 0 15 11"><rect x=".5" y=".5" width="14" height="8" fill="none" stroke="var(--icon)"/><rect x="4" y="10" width="7" height="1" fill="var(--icon)"/></svg></a>
  <a class="nav-item" style="left:799px"><svg width="14" height="10" viewBox="0 0 14 10"><circle cx="7" cy="3" r="2.5" fill="var(--icon)"/><path d="M2 10c0-3 2-4.5 5-4.5s5 1.5 5 4.5z" fill="var(--icon)"/><circle cx="2.5" cy="4" r="1.6" fill="var(--icon)"/><circle cx="11.5" cy="4" r="1.6" fill="var(--icon)"/></svg></a>
  <a class="nav-item" style="left:854px"><svg width="13" height="9" viewBox="0 0 13 9"><rect width="13" height="9" fill="var(--icon)"/><path d="M0 0l6.5 5L13 0" fill="none" stroke="var(--bar)"/></svg></a>
</header>

<div class="footer-band"></div>

<main>
  <div class="tile brand-tile"><span>veltrimo</span></div>
  <article class="card" style="left:316px;top:228px;width:135px;height:135px">
    <h3>We Design for Modern Medicine</h3>
    <p>Our design team specializes in creating modern sites developed to get current and potential patients the information they need.</p>
  </article>

  <section class="intro">
    <p>We are a small group of <b>designers</b>, <b>physicians</b> and <b>creatives</b> working together to deliver the <b>best experiences</b> in our market.</p>
    <span class="cta">Get Started</span>
  </section>

  <div class="media" role="img" aria-label="Clinic website screenshot with doctors" style="left:748px;top:83px;width:135px;height:87px;background:linear-gradient(135deg,#e9f1f6,#c9dbe6 60%,#4aa8d8)"></div>
  <article class="card" style="left:748px;top:180px;width:135px;height:183px">
    <h3>Print &amp; advertising are key</h3>
    <p>Our creative development and design teams focus on producing innovative print materials and ad campaigns to get you noticed.</p>
  </article>

  <div class="media" role="img" aria-label="Print brochure mockup for a wellness brand" style="left:316px;top:373px;width:135px;height:135px;background:linear-gradient(135deg,#bcc3c5,#e6ecec 55%,#9fd3cf)"></div>
  <article class="card" style="left:460px;top:373px;width:135px;height:135px">
    <h3>Struggling to earn more referrals?</h3>
    <p>Our team can provide market training to help your practice maximize the number of high quality referrals you receive.</p>
  </article>
  <div class="media" role="img" aria-label="Colourful printed stationery set" style="left:604px;top:373px;width:135px;height:135px;background:linear-gradient(135deg,#e2e2e2,#f2c2c8 50%,#e8e8e8)"></div>
  <div class="media" role="img" aria-label="Medical centre website layout in blue" style="left:748px;top:373px;width:135px;height:135px;background:linear-gradient(180deg,#f2f5f8 0,#5b9bd5 10%,#a9c9e6 55%,#1e5fa8 65%,#eef1f4 95%)"></div>

  <div class="media" role="img" aria-label="Portrait photo of a team member" style="left:316px;top:519px;width:135px;height:136px;background:linear-gradient(180deg,#a39582,#b9a38c 55%,#2ea4b8)"></div>
  <div class="media" role="img" aria-label="Portrait photo of a team member" style="left:460px;top:519px;width:135px;height:136px;background:linear-gradient(180deg,#d8d5cf,#a26e4e 60%,#e9e6e1)"></div>

  <section class="project">
    <h2>Projeto Web para a <em>Valdren / Corvexa</em><br>Indústria Farmacêutica</h2>
    <small>Valdren / Corvexa - International Pharmaceutical Industry (Web Project)</small>
    <div class="media" role="img" aria-label="Pharmaceutical website shown on a desktop screen" style="left:15px;top:95px;width:250px;height:186px;background:linear-gradient(180deg,#2b2b2b 0,#3b5c7e 12%,#8fb0cc 45%,#f2f2f2 60%,#f2f2f2 88%,#c9c9c9 100%)"></div>
  </section>

  <div class="media" role="img" aria-label="Mobile app on a phone held in a hand" style="left:316px;top:665px;width:135px;height:135px;background:linear-gradient(135deg,#f4f4f4,#e63a67 50%,#efe8e4)"></div>
  <div class="media" role="img" aria-label="Teal clinic website with a nurse" style="left:460px;top:665px;width:135px;height:135px;background:linear-gradient(180deg,#16b3bf,#1aa7b3 40%,#dfeff1 60%,#17b0bd)"></div>

  <div class="media" role="img" aria-label="Dark street map with office location" style="left:316px;top:809px;width:288px;height:135px;background:radial-gradient(circle at 50% 45%,#3a3a3a,#2b2b2b 70%)"></div>

  <section class="contact">
    <h2>veltrimo</h2>
    <ul>
      <li><svg viewBox="0 0 18 8" height="8"><rect width="9" height="7" fill="#bbb"/><path d="M0 0l4.5 3.5L9 0" fill="none" stroke="#262626"/></svg>info@veltrimo.com</li>
      <li><svg viewBox="0 0 18 8" height="8"><path d="M1 0h2l1 2-1.3 1a5 5 0 0 0 2.3 2.3L6 4l2 1v2c-4 1-8-3-7-7z" fill="#bbb"/></svg>+12 4410 2276</li>
      <li><svg viewBox="0 0 18 8" height="8"><path d="M4.5 0 0 4h1.2v4h2.3V5.5h2V8h2.3V4H9z" fill="#bbb"/></svg>14 Arden Row, Halsbury, Kent, UK</li>
    </ul>
  </section>
</main>

<footer>
  <div class="copyright">©2014 veltrimo</div>
  <span class="social" style="left:830px"></span>
  <span class="social" style="left:853px"></span>
  <span class="social" style="left:877px"></span>
</footer>
</body>
</html>
```